Facebook Header Design Project.

I'm supplying white and colored logos. The Facebook page already exists. URL = https://www.examplesocial.test/lumacrest.design The design should not be based on what's already there. Consider mobile implications of the design. This Design will form the designs of other social media headers. LumaCrest is a web design | digital marketing company.

Target Market(s)

People interested in web design | digital marketing services.

Industry/Entity Type

LumaCrest is a web design | digital marketing company. That should be clear in the design.

Colors
0054AA
0677BA
7BADD7
CADEEF
E8F1F8

Requirements
Must have
• Logo. Use Facebook header image dimension.
Nice to have
• Use a color scheme like the logo and feel free to add a color or two from the other side of the color whee.

```html
<!DOCTYPE html>
<html lang="en">
<head>
<meta charset="utf-8">
<title>LumaCrest — Cover</title>
<link rel="stylesheet" href="https://fonts.googleapis.com/css2?family=Arimo:wght@700&display=swap">
<style>
  :root {
    --navy: #0a3a85;
    --navy-deep: #062f73;
    --bg-light: #f7f7f8;
    --bg-mid: #ebebed;
    --bg-dark: #dedee0;
    --white: #ffffff;
  }
  * { margin: 0; padding: 0; box-sizing: border-box; }
  html, body { width: 1200px; height: 457px; overflow: hidden; }
  body { font-family: "Arimo", Arial, sans-serif; }

  .cover {
    position: relative;
    width: 1200px;
    height: 457px;
    overflow: hidden;
  }

  .backdrop {
    position: absolute;
    inset: 0;
    background:
      radial-gradient(ellipse 60% 70% at 55% 30%, var(--bg-light) 0%, transparent 70%),
      linear-gradient(180deg, var(--bg-dark) 0%, var(--bg-mid) 35%, var(--bg-light) 75%, var(--white) 100%);
  }

  .brand-name {
    position: absolute;
    left: 0;
    width: 1210px;
    top: 168px;
    text-align: center;
    font-size: 104px;
    line-height: 1;
    font-weight: 700;
    color: var(--navy);
    letter-spacing: -1px;
  }

  .tagline {
    position: absolute;
    left: 0;
    width: 1200px;
    top: 393px;
    text-align: center;
    font-size: 21px;
    font-weight: 700;
    letter-spacing: 1.6px;
    color: var(--navy-deep);
    line-height: 1;
  }

  .contact-row { list-style: none; }
  .contact-item {
    position: absolute;
    top: 423px;
    display: flex;
    align-items: center;
    gap: 7px;
    font-size: 9px;
    font-weight: 700;
    color: var(--navy-deep);
    line-height: 1;
  }
  .contact-item--phone { left: 420px; }
  .contact-item--web { left: 526px; }
  .contact-item--email { left: 659px; }
  .contact-icon { width: 20px; height: 20px; display: block; }
</style>
</head>
<body>
<main class="cover">
  <div class="backdrop" role="img" aria-label="Soft light grey gradient background with faint tech line pattern"></div>

  <h1 class="brand-name">LumaCrest</h1>

  <p class="tagline">WEB DESIGN | DIGITAL MARKETING</p>

  <ul class="contact-row">
    <li class="contact-item contact-item--phone">
      <svg class="contact-icon" viewBox="0 0 24 24" aria-hidden="true">
        <circle cx="12" cy="12" r="12" fill="var(--navy-deep)"/>
        <path d="M8.2 5.8c.5-.3 1.1-.2 1.4.3l1.3 2.1c.3.5.2 1.1-.3 1.4l-.9.6c.5 1.5 1.6 2.8 3.1 3.6l.7-.8c.4-.4 1-.5 1.5-.2l2 1.4c.5.3.6 1 .2 1.4l-1 1.2c-.6.7-1.6 1-2.5.6-3.1-1.3-5.5-3.8-6.6-7-.3-.9 0-1.9.7-2.5z" fill="var(--white)"/>
      </svg>
      <span>YOUR PHONE</span>
    </li>
    <li class="contact-item contact-item--web">
      <svg class="contact-icon" viewBox="0 0 24 24" aria-hidden="true">
        <circle cx="12" cy="12" r="12" fill="var(--navy-deep)"/>
        <g fill="none" stroke="var(--white)" stroke-width="1.3">
          <circle cx="12" cy="12" r="6.5"/>
          <ellipse cx="12" cy="12" rx="2.8" ry="6.5"/>
          <line x1="5.5" y1="12" x2="18.5" y2="12"/>
        </g>
      </svg>
      <span>YOUR WEB ADDRESS</span>
    </li>
    <li class="contact-item contact-item--email">
      <svg class="contact-icon" viewBox="0 0 24 24" aria-hidden="true">
        <circle cx="12" cy="12" r="12" fill="var(--navy-deep)"/>
        <rect x="6" y="8" width="12" height="8.5" rx="1" fill="none" stroke="var(--white)" stroke-width="1.3"/>
        <polyline points="6.3,8.5 12,13 17.7,8.5" fill="none" stroke="var(--white)" stroke-width="1.3"/>
      </svg>
      <span>YOUR EMAIL ADDRESS</span>
    </li>
  </ul>
</main>
</body>
</html>
```